Original Cellphone and Tablet Accesories

We are Vorel SAS, we sell the biggest brands in cell phone accesories like Kelvora, Brimcase, Tavlo, Muri, Clanwick, Hardmesa, DPN, Volantu,Drune, Plomak and we are about to release our magento ecommerce.

We would like to see website designs according to our corporate image (file attached)

User needs to be able to search by Cell phone(device), like Zenfon 5R, by Brand, like Brimcase and by Category like Cases. We need responsive and revolutionary design, this is the most important part for catch client in our site.

We Like lastest device design (2)

We like Top menus with pic (1)

Home should have:

Best Sellers
Lastest Devices
Lastest Arrivals
Space for our phone line

The product page has to have tabs for:
Compatibility
Specs

And this item on product page:
Email alerts: price drop, back in stock

We like 1 page checkout, but open to see new proposals (4)*
*This is very important, this is where clients buys or leaves site... I need big proposals here

We like big side to side banners (3)

We wants the cleanest design possible.

We want to transmit confidence, most this market here in Colombia is counterfeit products, so we want to transmit that we sell original brand products.

Attached file sent in spanish (clasificaciones y filtros) categories and filters, I hope this helps you for design.

Brands we sell reference sites:

www.volantu.example
www.brimcase.example
www.tavlo.example
http://www.kelvora.example/africa_en/consumer/mobile-phone/mobile-phone/mobile-phone-accessories/
http://store.muri.example/

Like design:

www.gadrilo.example

These are the market leaders world wide, don't like his design, but do like some or their filters and features:

http://www.handquarry.example/

Reference lastest devices:

Quorin Zenfon 5r
Kelvora Nimbar Slate 3
Kelvora Nimbar R4
Muri Veltano Q1
Muri Veltano Q Grande
Quorin Zenpad Lite
JRP Uno
DK P2
DK Ardent 5

Please focus on usability interface:
search by

device> category> brand
brand>device

the goal is the client get to the products they are looking for the easier way and see related items to get more sales.

Target Market(s)

Early adopters on new cell phone and tablet devices aged at 20-60, they likes to show off their new acquisition

Industry/Entity Type

Cell Phone

Colors
33a6d7
33a7d8
cee9f6
ffffff
ebf7f9
d9eff7

Requirements
Must have
• a design to filter by cell phone device, brand or category

website should communicate we sell original cell phone accessories, not counterfeit products

website should communicate we sell quality products

```html
<!DOCTYPE html>
<html lang="en">
<head>
<meta charset="utf-8">
<title>Vorel – Smart Phones & Tablets</title>
<link rel="stylesheet" href="https://fonts.googleapis.com/css2?family=Open+Sans:wght@400;600;700&family=Quicksand:wght@400;500;700&family=Oswald:wght@400;500;700&display=swap">
<style>
:root{
  --blue:#33a6d7;
  --blue-deep:#1192c8;
  --blue-sale:#0d9ccf;
  --ice:#cee9f6;
  --ice-2:#ebf7f9;
  --dark:#2f3132;
  --dark-2:#3a3d40;
  --grey-bg:#f0f0f0;
  --grey-line:#dcdcdc;
  --grey-panel:#b7b7b7;
  --text:#444;
  --muted:#8a8a8a;
  --green:#a6c33b;
  --purple:#5a3e8e;
  --star:#f2a516;
  --white:#fff;
}
*{box-sizing:border-box;margin:0;padding:0}
html,body{width:1200px;height:2707px;overflow:hidden}
body{position:relative;background:var(--white);font-family:"Open Sans",Arial,sans-serif;color:var(--text)}
.abs{position:absolute}
a{color:inherit;text-decoration:none}

/* top bar */
.topbar{left:0;top:0;width:1200px;height:40px;background:var(--dark)}
.topbar-link{position:absolute;top:11px;font-size:12px;color:var(--white);display:flex;align-items:center;gap:8px}
.topbar-link svg{width:13px;height:13px;fill:var(--white)}

/* header */
.logo{left:121px;top:76px;display:flex;align-items:center;gap:18px}
.logo-dot{width:70px;height:70px;border-radius:50%;border:5px solid var(--blue)}
.logo-name{font-family:"Quicksand",sans-serif;font-weight:400;font-size:62px;letter-spacing:10px;color:var(--blue)}
.call{left:838px;top:78px;display:flex;align-items:center;gap:10px;font-family:"Quicksand",sans-serif;font-size:24px;color:var(--dark);font-weight:500}
.call span{color:var(--blue)}
.call svg{width:34px;height:34px}
.search-input{left:679px;top:132px;width:236px;height:34px;border:1px solid #cfcfcf;font-size:12px;color:#999;padding:9px 12px;font-style:italic}
.search-cat{left:925px;top:132px;width:105px;height:34px;border:1px solid #cfcfcf;font-size:12px;color:#999;padding:9px 10px;font-style:italic}
.search-cat:after,.select:after{content:"";position:absolute;right:10px;top:15px;border:4px solid transparent;border-top:5px solid #555}
.search-go{left:1041px;top:130px;width:37px;height:36px;background:var(--blue);color:var(--white);font-size:12px;font-weight:700;text-align:center;line-height:36px}

/* nav */
.mainnav{left:0;top:217px;width:1200px;height:47px;background:var(--dark)}
.nav-item{position:absolute;top:16px;font-size:12.5px;color:var(--white);text-transform:uppercase;letter-spacing:.3px;display:flex;align-items:center;gap:8px}
.nav-item svg{width:9px;height:9px}
.nav-home{left:124px;top:12px}

/* hero */
.hero{left:121px;top:303px;width:712px;height:353px;background:#f3f3f3;border:1px solid #e2e2e2}
.hero-kicker{left:20px;top:60px;font-family:"Quicksand",sans-serif;font-size:29px;color:var(--blue-deep)}
.hero-title{left:20px;top:94px;font-family:"Quicksand",sans-serif;font-size:29px;font-weight:700;color:var(--blue-deep);letter-spacing:.5px}
.hero-sub{left:20px;top:140px;font-family:"Quicksand",sans-serif;font-size:18px;color:#666}
.hero-copy{left:20px;top:170px;width:320px;font-size:13px;line-height:21px;color:#333}
.hero-btn{left:22px;top:246px;width:183px;height:34px;background:var(--dark);color:var(--white);font-size:12px;text-align:center;line-height:34px;border-radius:2px}
.hero-visual{left:360px;top:40px;width:335px;height:280px;background:linear-gradient(135deg,#e8e8e8,#9aa0a8 55%,#3c3f44);border-radius:12px}

.finder{left:851px;top:303px;width:226px;height:353px;background:var(--grey-panel)}
.finder-head{left:845px;top:332px;width:240px;height:34px;background:var(--blue-sale);color:var(--white);font-size:18px;font-weight:600;letter-spacing:1px;text-align:center;line-height:34px}
.select{position:absolute;left:17px;width:193px;height:38px;background:var(--white);border-radius:2px;font-size:12px;font-style:italic;color:#666;padding:11px 13px}
.find-btn{left:73px;top:294px;width:81px;height:31px;background:var(--purple);color:var(--white);font-size:14px;font-weight:700;text-align:center;line-height:31px}

/* section bars */
.bar{left:121px;width:956px;height:36px;background:var(--dark)}
.bar-icon{position:absolute;left:0;top:0;width:48px;height:36px;background:var(--blue);display:flex;align-items:center;justify-content:center}
.bar-icon svg{width:20px;height:20px}
.bar-title{position:absolute;left:74px;top:10px;font-size:13px;font-weight:700;color:var(--white);letter-spacing:.6px;text-transform:uppercase}
.bar-arrows{position:absolute;right:14px;top:9px;display:flex;gap:6px}
.bar-arrows span{width:18px;height:18px;border-radius:50%;background:#999;display:flex;align-items:center;justify-content:center}
.bar-arrows svg{width:8px;height:8px}

/* latest devices */
.device{position:absolute;top:767px;width:226px;height:271px}
.device-shot{position:absolute;left:0;top:0;width:226px;height:211px;background:var(--white);border:1px solid #f0f0f0}
.device-phone{position:absolute;left:50%;top:16px;width:94px;height:180px;margin-left:-47px;border-radius:12px;background:linear-gradient(160deg,#4a5058,#101214)}
.sale-tag{position:absolute;left:14px;top:0;width:29px;height:67px;background:var(--green)}
.sale-tag:after{content:"";position:absolute;bottom:-1px;left:0;border-left:14.5px solid transparent;border-right:14.5px solid transparent;border-bottom:9px solid var(--white)}
.sale-tag span{position:absolute;left:7px;top:34px;transform:rotate(-90deg);transform-origin:0 0;font-size:11px;font-weight:700;color:var(--white);letter-spacing:1px;left:8px;top:42px}
.device-info{position:absolute;left:0;top:211px;width:226px;height:60px;background:#efefef;padding:8px 10px}
.device-name{font-size:13px;color:#666;text-transform:uppercase}
.device-price{display:flex;align-items:center;margin-top:4px;font-size:15px;color:var(--blue)}
.device-price s{font-size:10px;color:#888;margin-right:6px}
.stars{margin-left:auto;display:flex;gap:1px}
.stars svg{width:11px;height:11px}

/* latest arrivals */
.arrivals{left:121px;top:1144px;width:956px;height:293px;background:var(--grey-bg)}
.arrival{position:absolute;top:62px;width:162px;height:195px;background:var(--white);border:1px solid #e0e0e0;text-align:center}
.arrival-shot{position:absolute;left:50%;top:14px;margin-left:-27px;width:54px;height:106px;border-radius:7px}
.arrival-name{position:absolute;left:0;right:0;top:134px;font-size:12.5px;color:#555;letter-spacing:.5px}
.arrival-price{position:absolute;left:0;right:0;top:157px;font-size:17px;color:var(--blue)}
.arrival-price s{font-size:11px;color:#666;margin-left:6px}

/* brand / best sellers */
.panel-head{height:36px;color:var(--white);font-size:13px;font-weight:700;padding:10px 18px;letter-spacing:.4px;text-transform:uppercase}
.by-brand{left:121px;top:1493px;width:552px;height:334px;background:var(--grey-bg)}
.by-brand .panel-head{background:var(--dark)}
.brand-card{position:absolute;top:90px;width:155px;height:206px;background:var(--white);border:1px solid #e0e0e0;text-align:center}
.brand-card .arrival-shot{top:22px}
.brand-card .arrival-name{top:140px;font-size:12px}
.brand-price{position:absolute;left:34px;top:164px;width:86px;height:22px;background:var(--dark);color:var(--white);font-size:11px;line-height:22px}

.best{left:704px;top:1493px;width:366px;height:334px;background:var(--grey-bg)}
.best .panel-head{background:var(--blue-deep)}
.pager{position:absolute;right:22px;top:64px;display:flex;gap:6px;align-items:center;font-size:10px;color:#888}
.pager span{display:inline-block;height:18px;line-height:16px;padding:0 5px;border:1px solid #ccc;background:var(--white);color:#555}
.pager .on{background:var(--dark);color:var(--white);border-color:var(--dark)}
.pager .plain{border:0;background:none;font-style:italic;color:#999}
.seller{position:absolute;top:104px;width:151px;height:203px;background:var(--white);border:1px solid #ddd;text-align:center}
.seller-shot{position:absolute;left:50%;top:22px;margin-left:-28px;width:56px;height:92px;border-radius:8px;background:linear-gradient(160deg,#d6dbe0,#6f7780)}
.new-badge{position:absolute;right:-12px;top:-14px;width:42px;height:42px;border-radius:50%;background:var(--green);color:var(--white);font-size:10px;line-height:42px;font-weight:600}
.seller-name{position:absolute;left:0;right:0;top:124px;font-family:"Quicksand",sans-serif;font-size:14px;color:#333}
.seller-date{position:absolute;left:0;right:0;top:146px;font-size:8.5px;color:var(--blue)}
.seller-btn{position:absolute;left:16px;top:165px;width:118px;height:26px;background:var(--dark);color:var(--white);font-size:9.5px;font-weight:700;line-height:26px}

/* big sale */
.promo{left:125px;top:1866px;width:548px;height:275px;background:var(--blue-sale);text-align:center;color:var(--white);font-family:"Oswald",sans-serif}
.promo-dates{position:absolute;left:0;right:0;top:32px;font-size:25px;font-weight:400;letter-spacing:.3px}
.promo-title{position:absolute;left:0;right:0;top:64px;font-size:92px;font-weight:700;line-height:1;letter-spacing:2px}
.promo-rate{position:absolute;left:187px;top:181px;width:173px;height:54px;background:var(--white);color:var(--blue-sale);font-size:40px;font-weight:500;line-height:54px}

.feeds{left:704px;top:1864px;width:365px;height:277px;background:var(--grey-bg);border:1px solid #ddd}
.feeds-head{position:absolute;left:0;right:0;top:0;height:52px;padding:15px 22px;border-bottom:1px solid #ddd;font-size:16px;color:#444;letter-spacing:1px;text-transform:uppercase}
.feed{position:absolute;left:54px;width:290px;height:83px;background:var(--white);border:1px solid #dcdcdc;padding:10px 18px;font-size:10.5px;line-height:18px;color:#333}
.feed-date{position:absolute;right:16px;bottom:6px;font-size:9px;color:#666}
.feed-dot{position:absolute;left:18px;width:22px;height:22px;border-radius:50%;background:var(--blue-sale)}

/* brands */
.brands-label{left:130px;top:2187px;font-size:15px;font-weight:600;color:#333;letter-spacing:1.5px;text-transform:uppercase}
.rule{left:130px;width:946px;height:1px;background:var(--grey-line)}
.brand-name{position:absolute;top:2273px;font-size:22px;font-weight:700;color:#444;letter-spacing:1px;text-transform:uppercase;transform:translateX(-50%)}

/* footer */
.footer{left:0;top:2395px;width:1200px;height:244px;background:var(--grey-bg)}
.foot-col{position:absolute;top:46px}
.foot-col h4{font-size:11.5px;font-weight:600;color:var(--blue);text-transform:uppercase;margin-bottom:12px}
.foot-col li{list-style:none;font-size:11.5px;color:#999;line-height:23px}
.foot-phone{display:flex;gap:14px}
.foot-phone svg{width:34px;height:34px;margin-top:12px}
.bottombar{left:0;top:2639px;width:1200px;height:68px;background:var(--dark-2)}
.powered{position:absolute;left:125px;top:27px;font-size:10px;color:#bbb}
.socials{position:absolute;left:968px;top:22px;display:flex;gap:9px}
.socials span{width:20px;height:20px;border-radius:50%;background:var(--white)}
</style>
</head>
<body>

<!-- top bar -->
<div class="abs topbar">
  <a class="topbar-link" style="left:562px"><svg viewBox="0 0 16 16"><rect x="3" y="7" width="10" height="8" rx="1"/><path d="M5 7V5a3 3 0 0 1 6 0v2" fill="none" stroke="#fff" stroke-width="2"/></svg>Log In</a>
  <a class="topbar-link" style="left:645px"><svg viewBox="0 0 16 16"><rect x="2" y="2" width="12" height="12" rx="1"/></svg>My Wishlist</a>
  <a class="topbar-link" style="left:750px"><svg viewBox="0 0 16 16"><circle cx="8" cy="5" r="3.5"/><path d="M1 16c0-4 3-6 7-6s7 2 7 6z"/></svg>My Account</a>
  <a class="topbar-link" style="left:859px"><svg viewBox="0 0 16 16"><path d="M0 2h3l2 8h9l2-6H5" fill="none" stroke="#fff" stroke-width="1.8"/><circle cx="6" cy="14" r="1.6"/><circle cx="13" cy="14" r="1.6"/></svg>My Cart (0) Items</a>
  <a class="topbar-link" style="left:1004px"><svg viewBox="0 0 16 16"><path d="M3 2l11 6-11 6z"/></svg>Checkout</a>
</div>

<!-- header -->
<div class="abs logo"><span class="logo-dot"></span><span class="logo-name">VOREL</span></div>
<div class="abs call">
  <svg viewBox="0 0 34 34"><circle cx="17" cy="17" r="15" fill="none" stroke="#33a6d7" stroke-width="2.5"/><path d="M11 9c1-1 2-1 3 0l2 3c.6 1 .3 1.6-.5 2.3l-1 .8c.8 2 2.5 3.7 4.5 4.5l.8-1c.7-.8 1.3-1.1 2.3-.5l3 2c1 1 1 2 0 3l-1.5 1.5C20 26 8 14 9.5 10.5z" fill="#33a6d7"/></svg>
  CALL : <span>555-010-7890</span>
</div>
<div class="abs search-input">Search</div>
<div class="abs search-cat">Categories</div>
<div class="abs search-go">GO</div>

<!-- main navigation -->
<nav class="abs mainnav">
  <a class="nav-item nav-home"><svg viewBox="0 0 24 22" style="width:26px;height:24px"><path d="M12 1L1 11h3v10h6v-6h4v6h6V11h3z" fill="#fff"/></svg></a>
  <a class="nav-item" style="left:197px">Smartphones</a>
  <a class="nav-item" style="left:331px">Computer &amp; Tablets <svg viewBox="0 0 10 10"><path d="M1 3l4 4 4-4" stroke="#fff" stroke-width="2" fill="none"/></svg></a>
  <a class="nav-item" style="left:510px">Brands <svg viewBox="0 0 10 10"><path d="M1 3l4 4 4-4" stroke="#fff" stroke-width="2" fill="none"/></svg></a>
  <a class="nav-item" style="left:597px">Accessories <svg viewBox="0 0 10 10"><path d="M1 3l4 4 4-4" stroke="#fff" stroke-width="2" fill="none"/></svg></a>
  <a class="nav-item" style="left:726px">Support</a>
  <a class="nav-item" style="left:821px">About</a>
  <a class="nav-item" style="left:908px">Contact</a>
</nav>

<!-- hero -->
<section class="abs hero">
  <div class="abs hero-kicker">Launch</div>
  <div class="abs hero-title">Smart Phones Tables</div>
  <div class="abs hero-sub">Smart and Design</div>
  <p class="abs hero-copy">Lorem ipsum dolor sit amet, consectetur ipsum adipisicing elit, sed do eiusmod tempor incididunt ut labore et dolore magna aliqua. Ut</p>
  <a class="abs hero-btn">Discover More Launch</a>
  <div class="abs hero-visual" role="img" aria-label="Group of smartphones and tablets showing colourful home screens"></div>
</section>

<aside class="abs finder">
  <div class="select" style="top:99px">Select Category</div>
  <div class="select" style="top:161px">Select Brand</div>
  <div class="select" style="top:220px">Select Device</div>
  <a class="abs find-btn">FIND</a>
</aside>
<div class="abs finder-head">SEARCH</div>

<!-- latest devices -->
<div class="abs bar" style="top:691px">
  <span class="bar-icon"><svg viewBox="0 0 20 20"><path d="M10 2l2.4 5.2 5.6.6-4.2 3.8 1.2 5.6L10 14.4 5 17.2l1.2-5.6L2 7.8l5.6-.6z" fill="none" stroke="#fff" stroke-width="1.4"/></svg></span>
  <span class="bar-title">Latest Devices</span>
  <span class="bar-arrows"><span><svg viewBox="0 0 8 8"><path d="M6 0L1 4l5 4z" fill="#333"/></svg></span><span><svg viewBox="0 0 8 8"><path d="M2 0l5 4-5 4z" fill="#333"/></svg></span></span>
</div>

<div class="device" style="left:125px">
  <div class="device-shot"><div class="device-phone" role="img" aria-label="Black touchscreen smartphone"></div></div>
  <div class="sale-tag"><span>SALE</span></div>
  <div class="device-info"><div class="device-name">Fusce Aliquam</div>
    <div class="device-price"><s>$170.00</s>$169.00<span class="stars"><svg viewBox="0 0 10 10"><path d="M5 0l1.5 3.2 3.5.4-2.6 2.4.7 3.5L5 7.8 1.9 9.5l.7-3.5L0 3.6l3.5-.4z" fill="#f2a516"/></svg><svg viewBox="0 0 10 10"><path d="M5 0l1.5 3.2 3.5.4-2.6 2.4.7 3.5L5 7.8 1.9 9.5l.7-3.5L0 3.6l3.5-.4z" fill="#f2a516"/></svg><svg viewBox="0 0 10 10"><path d="M5 0l1.5 3.2 3.5.4-2.6 2.4.7 3.5L5 7.8 1.9 9.5l.7-3.5L0 3.6l3.5-.4z" fill="#f2a516"/></svg><svg viewBox="0 0 10 10"><path d="M5 0l1.5 3.2 3.5.4-2.6 2.4.7 3.5L5 7.8 1.9 9.5l.7-3.5L0 3.6l3.5-.4z" fill="#f2a516"/></svg><svg viewBox="0 0 10 10"><path d="M5 0l1.5 3.2 3.5.4-2.6 2.4.7 3.5L5 7.8 1.9 9.5l.7-3.5L0 3.6l3.5-.4z" fill="#aaa"/></svg></span></div></div>
</div>
<div class="device" style="left:366px">
  <div class="device-shot"><div class="device-phone" role="img" aria-label="Dark smartphone with colourful wallpaper" style="background:linear-gradient(160deg,#3b4a5c,#1b2530)"></div></div>
  <div class="sale-tag"><span>SALE</span></div>
  <div class="device-info"><div class="device-name">Quisque In Arcu</div>
    <div class="device-price">$800.00<span class="stars"><svg viewBox="0 0 10 10"><path d="M5 0l1.5 3.2 3.5.4-2.6 2.4.7 3.5L5 7.8 1.9 9.5l.7-3.5L0 3.6l3.5-.4z" fill="#f2a516"/></svg><svg viewBox="0 0 10 10"><path d="M5 0l1.5 3.2 3.5.4-2.6 2.4.7 3.5L5 7.8 1.9 9.5l.7-3.5L0 3.6l3.5-.4z" fill="#f2a516"/></svg><svg viewBox="0 0 10 10"><path d="M5 0l1.5 3.2 3.5.4-2.6 2.4.7 3.5L5 7.8 1.9 9.5l.7-3.5L0 3.6l3.5-.4z" fill="#f2a516"/></svg><svg viewBox="0 0 10 10"><path d="M5 0l1.5 3.2 3.5.4-2.6 2.4.7 3.5L5 7.8 1.9 9.5l.7-3.5L0 3.6l3.5-.4z" fill="#f2a516"/></svg><svg viewBox="0 0 10 10"><path d="M5 0l1.5 3.2 3.5.4-2.6 2.4.7 3.5L5 7.8 1.9 9.5l.7-3.5L0 3.6l3.5-.4z" fill="#aaa"/></svg></span></div></div>
</div>
<div class="device" style="left:608px">
  <div class="device-shot"><div class="device-phone" role="img" aria-label="Black rectangular smartphone"></div></div>
  <div class="sale-tag"><span>SALE</span></div>
  <div class="device-info"><div class="device-name">Proin Lectus Ipsum</div>
    <div class="device-price">$450.00<span class="stars"><svg viewBox="0 0 10 10"><path d="M5 0l1.5 3.2 3.5.4-2.6 2.4.7 3.5L5 7.8 1.9 9.5l.7-3.5L0 3.6l3.5-.4z" fill="#f2a516"/></svg><svg viewBox="0 0 10 10"><path d="M5 0l1.5 3.2 3.5.4-2.6 2.4.7 3.5L5 7.8 1.9 9.5l.7-3.5L0 3.6l3.5-.4z" fill="#f2a516"/></svg><svg viewBox="0 0 10 10"><path d="M5 0l1.5 3.2 3.5.4-2.6 2.4.7 3.5L5 7.8 1.9 9.5l.7-3.5L0 3.6l3.5-.4z" fill="#f2a516"/></svg><svg viewBox="0 0 10 10"><path d="M5 0l1.5 3.2 3.5.4-2.6 2.4.7 3.5L5 7.8 1.9 9.5l.7-3.5L0 3.6l3.5-.4z" fill="#f2a516"/></svg><svg viewBox="0 0 10 10"><path d="M5 0l1.5 3.2 3.5.4-2.6 2.4.7 3.5L5 7.8 1.9 9.5l.7-3.5L0 3.6l3.5-.4z" fill="#aaa"/></svg></span></div></div>
</div>
<div class="device" style="left:851px">
  <div class="device-shot"><div class="device-phone" role="img" aria-label="Black smartphone with app icon grid"></div></div>
  <div class="sale-tag"><span>SALE</span></div>
  <div class="device-info"><div class="device-name">Proin Lectus Ipsum</div>
    <div class="device-price">$450.00<span class="stars"><svg viewBox="0 0 10 10"><path d="M5 0l1.5 3.2 3.5.4-2.6 2.4.7 3.5L5 7.8 1.9 9.5l.7-3.5L0 3.6l3.5-.4z" fill="#f2a516"/></svg><svg viewBox="0 0 10 10"><path d="M5 0l1.5 3.2 3.5.4-2.6 2.4.7 3.5L5 7.8 1.9 9.5l.7-3.5L0 3.6l3.5-.4z" fill="#f2a516"/></svg><svg viewBox="0 0 10 10"><path d="M5 0l1.5 3.2 3.5.4-2.6 2.4.7 3.5L5 7.8 1.9 9.5l.7-3.5L0 3.6l3.5-.4z" fill="#f2a516"/></svg><svg viewBox="0 0 10 10"><path d="M5 0l1.5 3.2 3.5.4-2.6 2.4.7 3.5L5 7.8 1.9 9.5l.7-3.5L0 3.6l3.5-.4z" fill="#f2a516"/></svg><svg viewBox="0 0 10 10"><path d="M5 0l1.5 3.2 3.5.4-2.6 2.4.7 3.5L5 7.8 1.9 9.5l.7-3.5L0 3.6l3.5-.4z" fill="#aaa"/></svg></span></div></div>
</div>

<!-- latest arrivals -->
<div class="abs bar" style="top:1112px">
  <span class="bar-icon"><svg viewBox="0 0 20 20"><path d="M10 2l2.4 5.2 5.6.6-4.2 3.8 1.2 5.6L10 14.4 5 17.2l1.2-5.6L2 7.8l5.6-.6z" fill="none" stroke="#fff" stroke-width="1.4"/></svg></span>
  <span class="bar-title">Latest Arrivals</span>
</div>
<section class="abs arrivals">
  <div class="arrival" style="left:36px"><div class="arrival-shot" role="img" aria-label="Dark smartphone" style="background:linear-gradient(160deg,#5a5f66,#1c1e21)"></div><div class="arrival-name">ECCOENWSM SUCAL</div><div class="arrival-price">$ 330.99<s>$ 330.99</s></div></div>
  <div class="arrival" style="left:219px"><div class="arrival-shot" role="img" aria-label="Purple-screen smartphone" style="background:linear-gradient(160deg,#5b5fb0,#1a1b3a)"></div><div class="arrival-name">ECCOENWSM SUCAL</div><div class="arrival-price">$ 330.99<s>$ 330.99</s></div></div>
  <div class="arrival" style="left:401px"><div class="arrival-shot" role="img" aria-label="Dark smartphone" style="background:linear-gradient(160deg,#5a5f66,#1c1e21)"></div><div class="arrival-name">ECCOENWSM SUCAL</div><div class="arrival-price">$ 330.99<s>$ 330.99</s></div></div>
  <div class="arrival" style="left:583px"><div class="arrival-shot" role="img" aria-label="White phablet with orange screen and stylus" style="background:linear-gradient(160deg,#f4a24a,#c9372d)"></div><div class="arrival-name">ECCOENWSM SUCAL</div><div class="arrival-price">$ 330.99<s>$ 330.99</s></div></div>
  <div class="arrival" style="left:769px"><div class="arrival-shot" role="img" aria-label="Purple-screen smartphone" style="background:linear-gradient(160deg,#5b5fb0,#1a1b3a)"></div><div class="arrival-name">ECCOENWSM SUCAL</div><div class="arrival-price">$ 330.99<s>$ 330.99</s></div></div>
</section>

<!-- products by brand -->
<section class="abs by-brand">
  <div class="panel-head">Products by Brand</div>
  <div class="brand-card" style="left:19px"><div class="arrival-shot" role="img" aria-label="Black smartphone" style="background:linear-gradient(160deg,#4a5058,#101214)"></div><div class="arrival-name">ECCOENWSM SUCAL</div><div class="brand-price">$ 330.99</div></div>
  <div class="brand-card" style="left:195px"><div class="arrival-shot" role="img" aria-label="Purple-screen smartphone" style="background:linear-gradient(160deg,#5b5fb0,#1a1b3a)"></div><div class="arrival-name">ECCOENWSM SUCAL</div><div class="brand-price">$ 330.99</div></div>
  <div class="brand-card" style="left:370px"><div class="arrival-shot" role="img" aria-label="Dark smartphone" style="background:linear-gradient(160deg,#5a5f66,#1c1e21)"></div><div class="arrival-name">ECCOENWSM SUCAL</div><div class="brand-price">$ 330.99</div></div>
</section>

<!-- best sellers -->
<section class="abs best">
  <div class="panel-head">Best Sellers</div>
  <div class="pager"><span class="plain">&lt; Prev</span><span class="on">1</span><span>2</span><span>Next &gt;</span></div>
  <div class="seller" style="left:18px"><div class="seller-shot" role="img" aria-label="Silver phablet with stylus"></div><div class="new-badge">New</div><div class="seller-name">Nimbar Slate II</div><div class="seller-date">Launching on 2/3/2014</div><div class="seller-btn">Read Specification</div></div>
  <div class="seller" style="left:188px"><div class="seller-shot" role="img" aria-label="White phablet with orange screen" style="background:linear-gradient(160deg,#f4a24a,#c9372d)"></div><div class="new-badge">New</div><div class="seller-name">Nimbar Slate III</div><div class="seller-date">Launching on 2/3/2014</div><div class="seller-btn">Read Specification</div></div>
</section>

<!-- promo -->
<section class="abs promo">
  <div class="promo-dates">FROM JANUARY 15th TO JULY 10th</div>
  <div class="promo-title">BIG SALE</div>
  <div class="promo-rate">30-50%</div>
</section>

<!-- feeds -->
<section class="abs feeds">
  <div class="feeds-head">Chirper Feeds</div>
  <span class="feed-dot" style="top:96px"></span>
  <div class="feed" style="top:66px">Hi guys, today Vorel brings you another #Deal phone Free Handset on this weekend. http://lnk.example/tQq5w<span class="feed-date">29 Jan</span></div>
  <span class="feed-dot" style="top:196px"></span>
  <div class="feed" style="top:166px">Hi guys, today Vorel brings you another #Deal phone Free Handset on this weekend. http://lnk.example/tQq5w<span class="feed-date">29 Jan</span></div>
</section>

<!-- our brands -->
<div class="abs brands-label">Our Brands</div>
<div class="abs rule" style="top:2238px"></div>
<span class="brand-name" style="left:177px">Kelvora</span>
<span class="brand-name" style="left:341px">Plomak</span>
<span class="brand-name" style="left:504px">Zendry</span>
<span class="brand-name" style="left:656px">Brimcase</span>
<span class="brand-name" style="left:818px">Casewell</span>
<span class="brand-name" style="left:1006px">Clearguard</span>
<div class="abs rule" style="top:2343px"></div>

<!-- footer -->
<footer class="abs footer">
  <div class="foot-col" style="left:121px"><h4>Information</h4><ul><li>About Us</li><li>Delivery Information</li><li>Privacy Policy</li><li>Terms &amp; Conditions</li></ul></div>
  <div class="foot-col" style="left:321px"><h4>Customer Service</h4><ul><li>Contact Us</li><li>Returns</li><li>Site Map</li></ul></div>
  <div class="foot-col" style="left:522px"><h4>Extras</h4><ul><li>Brands</li><li>Gift Vouchers</li><li>Affiliates</li><li>Specials</li></ul></div>
  <div class="foot-col" style="left:720px"><h4>My Account</h4><ul><li>My Account</li><li>Order History</li><li>Wish List</li><li>Newsletter</li></ul></div>
  <div class="foot-col" style="left:928px"><h4>Online Support</h4>
    <div class="foot-phone"><svg viewBox="0 0 34 34"><path d="M6 4c2-2 4-2 5 0l4 6c1 2 .5 3-1 4.5l-2 1.5c1.5 4 5 7.5 9 9l1.5-2c1.5-1.5 2.5-2 4.5-1l6 4c2 1 2 3 0 5l-3 3C20 36-4 12 3 7z" fill="#33a6d7"/></svg>
      <ul><li>1-800-555-0177</li><li>1-800-555-0178</li></ul></div>
  </div>
</footer>
<div class="abs bottombar">
  <span class="powered">Powered By Vorel Smart and desing © 2014</span>
  <span class="socials"><span></span><span></span><span></span><span></span></span>
</div>

</body>
</html>
```